Byteloft - Your IT support team - online sales website design concept

Byteloft aims to provide home and small business users with high quality, friendly and affordable IT support.

We are delivering this service through the website. Users will choose a support service that they want, enter some details, make a payment and then be connected to our support team member who will resolve their problem and discuss their IT with them by remotely controlling their computer and speaking to them on the phone.

This design project is to develop the website design concept which will:

# Give the user confidence that byteloft are a legitimate business giving premium yet good value IT support.
# Inform the users of our IT services.
# Encourage the user to try our services.
# Look fun, interesting, modern, respectable and trustworthy.

We intend to offer 4 core 'products' to our users, these are:
# Virus removal – We will clean your PC then protect it for the future
# Computer Speed Up – Optimise you PC to get the most out of it
# Skyvault your IT- auto backup of PC with remote access to documents, pictures, videos and email
# IT Support – to fix a problem or we can just help out

We are open to any fun or interesting ways of getting this message across to users.

We have the following idea which could be useful but does not have to be used in design concepts:

Perhaps a home/detached house on the front page with a cloud in the sky for our cloud service, a fast car on the drive or something to demonstrate computer speed up, a gremlin in the drain for virus removal and our byteloft yellow waves from our logo emanating towards the house as our general IT support offering. Maybe having some movement or information on mouse over.

We like the idea of real life images embedded into the page similar to this:

http://www.prolivasad.cz/

But, ideas could be cartoon based or whatever you think will look good. Any interesting concepts are welcome.

We want to have our 4 'products' clearly displayed on the home page. They could be in 4 boxes beneath some nice image or incorporated into a single nice image/cartoon or graphic. If incorporated into one graphic/cartoon/image we would have clickable areas of the image.

We want it to be clear to visitors what it is we are offering - IT support to remotely solve a computer/iPad/smartphone issue and that we are "Online now to fix your problem".

We might also want to feature 4 features/benefits:

UK Based Engineers (with GB flag)
Remote IT Support
Premium Support
Money Back Guarantee

We have a logo already which is attached. We would like a homepage design encompassing the features set out above, a second page design to be used as the main page when you click on one of the 4 'products' and also a general content page design so that we have a theme for the site. We just want these designs as images for this project.

Thank you for your interest.

Reason: 10 days was never long enough and we needed more time to respond to designers.

Reason: I've been away on holiday and I want some more time to respond to designers. Thanks, Colin

Target Market(s)

Home and small business users.

Industry/Entity Type

Small Business

Requirements
Must have
• We would like an area, to show whether we are open and online or not. When staff are available to deliver remote support the site should clearly show that staff are online working and available now to support. When we are offline the site should also show this.

We will offer our users a "Money Back Guarantee"; if they are not happy with the work that we do for them we will refund them.

```html
<!DOCTYPE html>
<html lang="en">
<head>
<meta charset="utf-8">
<title>Byteloft – your IT support team</title>
<link href="https://fonts.googleapis.com/css2?family=Open+Sans:ital,wght@0,400;0,600;0,700;1,400;1,700&display=swap" rel="stylesheet">
<style>
  :root {
    --band: #f3c458;
    --page-bg: #ebeae6;
    --panel: #fbfbfa;
    --ink: #4a4a4a;
    --ink-soft: #5a5a5a;
    --brand-yellow: #f2b21c;
    --link: #22b3d6;
    --green: #22b04a;
    --purple: #5b1f8e;
    --teal: #45bdb9;
    --orange: #f5891c;
    --icon-grey: #7b7b7b;
    --dark: #2f2f2f;
    --white: #ffffff;
  }
  * { margin: 0; padding: 0; box-sizing: border-box; }
  html, body { width: 1200px; height: 754px; overflow: hidden; }
  body {
    position: relative;
    background: var(--page-bg);
    font-family: "Open Sans", Arial, sans-serif;
    color: var(--ink);
  }
  .band {
    position: absolute; left: 0; width: 1200px;
    background: var(--band);
  }
  .band--top { top: 0; height: 53px; }
  .band--bottom { top: 698px; height: 56px; }
  .nav {
    position: absolute; left: 0; width: 1200px;
    display: flex; justify-content: center; gap: 20px;
    list-style: none;
  }
  .band--top .nav { top: 16px; }
  .band--bottom .nav { top: 20px; }
  .nav a {
    color: var(--white); text-decoration: none;
    font-size: 14px; letter-spacing: 0.2px;
  }
  .panel {
    position: absolute; left: 180px; top: 53px;
    width: 842px; height: 645px;
    background: var(--panel);
  }
  .brand {
    position: absolute; left: 0; top: 78px; width: 1200px;
    text-align: center;
  }
  .brand__name {
    display: inline-flex; align-items: center; gap: 8px;
    font-size: 38px; font-weight: 700; letter-spacing: -1px;
    color: var(--brand-yellow);
  }
  .brand__dot {
    width: 14px; height: 14px; border-radius: 50%;
    background: var(--brand-yellow);
  }
  .brand__tagline {
    margin-top: 6px; margin-left: 20px;
    font-size: 11px; font-style: italic; letter-spacing: 2.5px;
    color: var(--ink-soft);
  }
  .intro {
    position: absolute; left: 295px; top: 188px; width: 640px;
    font-size: 11.6px; font-weight: 700; line-height: 21.6px;
    color: var(--ink);
  }
  .intro a { color: var(--link); font-style: italic; }
  .product-art {
    position: absolute; top: 360px; width: 220px; height: 210px;
  }
  .product-art text {
    font-family: "Open Sans", Arial, sans-serif;
    font-size: 11px; font-weight: 700;
  }
  .product {
    position: absolute; top: 590px; height: 66px;
    padding-left: 16px;
    font-style: italic; font-size: 9.5px; line-height: 12px;
    color: var(--ink);
  }
  .product::before {
    content: ""; position: absolute; left: 0; top: 0;
    width: 7px; height: 66px; background: var(--accent);
  }
  .product__title { font-weight: 700; font-size: 10px; margin: 2px 0 12px; }
  .product--virus { left: 216px; --accent: var(--green); }
  .product--speed { left: 424px; --accent: var(--purple); }
  .product--cloud { left: 642px; --accent: var(--teal); }
  .product--support { left: 868px; --accent: var(--orange); }
  .social {
    position: absolute; left: 181px; top: 16px;
    display: flex; gap: 12px; list-style: none;
  }
  .social li {
    width: 22px; height: 22px; border-radius: 50%;
    background: var(--icon-grey);
  }
  .credit {
    position: absolute; left: 797px; top: 13px;
    display: flex; align-items: center; gap: 10px;
    font-size: 8.5px; font-weight: 600; color: var(--white);
  }
  .credit__mark { width: 31px; height: 31px; background: var(--dark); border-radius: 2px; }
</style>
</head>
<body>
  <header class="band band--top">
    <ul class="nav">
      <li><a href="#">Home</a></li>
      <li><a href="#">Product</a></li>
      <li><a href="#">Promotion</a></li>
      <li><a href="#">Contact Us</a></li>
    </ul>
  </header>

  <main class="panel"></main>

  <div class="brand">
    <div class="brand__name">byteloft <span class="brand__dot"></span></div>
    <div class="brand__tagline">your IT support team</div>
  </div>

  <p class="intro"><a href="#">Byteloft</a> aims to provide home and small business users with high quality, friendly and affordable IT support.<br>We are delivering this service through the website. Users will choose a support service that they want,<br>enter some details, make a payment and then be connected to our support team member who will resolve their<br>problem and discuss their IT with them through remotely controlling their computer and speaking to them<br>on the phone.</p>

  <svg class="product-art" style="left:170px" viewBox="0 0 220 210" role="img" aria-label="Virus removal illustration: green globe with signal waves and a virus">
    <defs><path id="arc-virus" d="M18 110 A92 92 0 0 0 80 190"/></defs>
    <circle cx="110" cy="110" r="62" fill="var(--green)"/>
    <text fill="var(--green)"><textPath href="#arc-virus">Virus Removal</textPath></text>
  </svg>
  <svg class="product-art" style="left:385px" viewBox="0 0 220 210" role="img" aria-label="Computer speed up illustration: purple globe with signal waves and a speed dial">
    <defs><path id="arc-speed" d="M18 120 A92 92 0 0 0 100 202"/></defs>
    <circle cx="110" cy="110" r="62" fill="var(--purple)"/>
    <text fill="var(--purple)"><textPath href="#arc-speed">Computer Speed Up</textPath></text>
  </svg>
  <svg class="product-art" style="left:595px" viewBox="0 0 220 210" role="img" aria-label="Skyvault illustration: glowing teal globe with signal waves and a cloud">
    <defs>
      <radialGradient id="glow" cx="0.45" cy="0.4" r="0.6">
        <stop offset="0" stop-color="#e9fbfb"/><stop offset="1" stop-color="var(--teal)"/>
      </radialGradient>
      <path id="arc-cloud" d="M18 120 A92 92 0 0 0 90 202"/>
    </defs>
    <circle cx="110" cy="110" r="62" fill="url(#glow)"/>
    <text fill="var(--teal)"><textPath href="#arc-cloud">Skyvault Your Life</textPath></text>
  </svg>
  <svg class="product-art" style="left:815px" viewBox="0 0 220 210" role="img" aria-label="IT support illustration: orange globe with signal waves and a wrench">
    <defs><path id="arc-support" d="M18 120 A92 92 0 0 0 60 185"/></defs>
    <circle cx="110" cy="110" r="62" fill="var(--orange)"/>
    <text fill="var(--orange)"><textPath href="#arc-support">IT Support</textPath></text>
  </svg>

  <section class="product product--virus">
    <h3 class="product__title">Virus Removal</h3>
    <p>We will clean your PC<br>then protect it for the future</p>
  </section>
  <section class="product product--speed">
    <h3 class="product__title">Computer Speed Up</h3>
    <p>Optimise you PC<br>to get the most out of it</p>
  </section>
  <section class="product product--cloud">
    <h3 class="product__title">Skyvault your Life</h3>
    <p>Auto backup of PC<br>and remote access to<br>files and email</p>
  </section>
  <section class="product product--support">
    <h3 class="product__title">IT Support</h3>
    <p>to fix a specific problem<br>or we can just help out</p>
  </section>

  <footer class="band band--bottom">
    <ul class="social" aria-label="Social links">
      <li></li><li></li><li></li>
    </ul>
    <ul class="nav">
      <li><a href="#">Home</a></li>
      <li><a href="#">Product</a></li>
      <li><a href="#">Promotion</a></li>
      <li><a href="#">Contact Us</a></li>
    </ul>
    <div class="credit">
      <span class="credit__mark"></span>
      <span>© 2013 Byteloft | powered by NetHarbor</span>
    </div>
  </footer>
</body>
</html>
```